Web and Logo Design for New Storvix T-shirt Store

I am opening a new online company called Brenquil to sell T-shirts. The website is brenquil.example. For the Menu heading it will be Home, Women, Men, About, Contact, Catalog. For the Categories, it will be Women, Men, T-shirt- Hoodies, Tank Tops, Long Sleeves. I will also need tshirt mockups for the landing page. Footer Menu: Home, About, Contact, Catalog, Shipping and Returns.
The colors to use for the website is #1D7D9E, #Black, #FBC326. For the logo, I will upload examples.
Heading Font: Calistoga.
Body Font: Raleway
Logo Font: Christopher Done.

HERE is an example of how I want my website: vortano.example, zib.example, kelvaro.example, printwhirl.example, threadloomy.example.

Target Market(s)

Young people

Industry/Entity Type

Clothing

Coding

Coded - Design and coding required

Number of Pages Required

5+ page

Font styles to use
Sans Serif
Decorative

Colors

Designer to choose colors to be used in the design.

Requirements
Must have
• A unique and creative logo and a stunning homepage.Please look at my website so that you have a feel of what I would like. I want my desgin to have the same page setup as my website.
The colors to use for the website is #1D7D9E, #Black, #FBC326.
Please Look at this link for example: https://shelfbay-quorntheme.example.com/
Nice to have
• Tshirt mockups for the homepage, Well use of colors, a homepage slider. A search box.
Should not have
• Don't use basic designs.

```html
<!DOCTYPE html>
<html lang="en">
<head>
<meta charset="utf-8">
<title>Brenquil — Login</title>
<link rel="stylesheet" href="https://fonts.googleapis.com/css2?family=Calistoga&family=Merriweather:wght@400&family=Raleway:wght@400;500;600;800&display=swap">
<style>
:root{
  --brand-blue:#1D7D9E;
  --brand-yellow:#FBC326;
  --ink:#111;
  --footer-dark:#333333;
  --band-grey:#f3f3f3;
  --line:#e3e3e3;
  --muted:#888;
}
*{box-sizing:border-box;margin:0;padding:0}
html,body{width:1200px;height:1082px;overflow:hidden;background:#fff;font-family:"Raleway",sans-serif;color:var(--ink)}
.page{position:relative;width:1200px;height:1082px}
.abs{position:absolute}
.topbar{left:0;top:0;width:1200px;height:37px;background:#000;color:#fff;font-size:13px}
.topbar .welcome{left:163px;top:11px}
.topbar .help{right:164px;top:11px;display:flex;align-items:center;gap:6px}
.topbar .help b{font-weight:600}
.brand{left:160px;top:62px;font-family:"Raleway",sans-serif;font-weight:800;font-size:44px;color:var(--brand-yellow);letter-spacing:1px}
.search{left:509px;top:54px;width:244px;height:32px;border:1px solid #bbb;border-radius:16px;background:#f4f4f4;font-size:12px;color:#444;padding:9px 0 0 17px}
.search .btn{position:absolute;right:3px;top:2px;width:26px;height:26px;border-radius:50%;background:var(--brand-blue);display:flex;align-items:center;justify-content:center}
.account{left:869px;top:60px;display:flex;align-items:center;gap:6px;font-size:14.5px;letter-spacing:.5px}
.cart{left:965px;top:60px;display:flex;align-items:center;gap:4px;font-size:14.5px;letter-spacing:.5px}
.cart .count{position:absolute;left:61px;top:-2px;width:14px;height:14px;border-radius:50%;background:var(--brand-blue);color:#fff;font-size:9px;text-align:center;line-height:14px}
.nav-rule{left:509px;top:103px;width:691px;height:1px;background:#ccc}
.mainnav{left:514px;top:114px;font-size:14px;letter-spacing:.3px}
.mainnav a{position:absolute;white-space:nowrap;color:var(--ink);text-decoration:none;display:flex;align-items:center;gap:5px}
.mainnav a.current{color:var(--brand-blue);font-weight:600}
.crumbs{left:0;top:141px;width:1200px;height:37px;background:var(--band-grey);font-size:12px}
.crumbs .trail{position:absolute;left:162px;top:13px;display:flex;gap:12px;align-items:center}
.crumbs .here{color:var(--brand-blue)}
.login-title{left:0;top:248px;width:1200px;text-align:center;font-family:"Calistoga",serif;font-weight:400;font-size:38px}
.login-card{left:373px;top:329px;width:455px;height:247px;border:1px solid var(--line)}
.field{position:absolute;left:44px;width:366px;height:38px;border:1px solid #ddd;display:flex;align-items:center}
.field .icon{width:44px;height:100%;border-right:1px solid #ddd;display:flex;align-items:center;justify-content:center}
.field .hint{padding-left:16px;font-size:12px;color:var(--muted);flex:1}
.field .eye{margin-right:14px}
.login-btn{position:absolute;left:173px;top:147px;width:108px;height:34px;background:var(--brand-blue);color:#fff;font-size:13px;font-weight:500;text-align:center;line-height:34px}
.card-links{position:absolute;left:44px;top:203px;width:366px;display:flex;justify-content:space-between;font-size:12px;color:#666}
.card-links a{color:var(--brand-blue);text-decoration:underline}
.site-footer{left:0;top:660px;width:1200px;height:369px;color:#fff}
.footer-brand{left:163px;top:808px;font-weight:800;font-size:40px;color:#fff;letter-spacing:1px}
.social{top:873px;width:30px;height:30px;border:1.5px solid #ddd;border-radius:50%}
.col-title{font-family:"Calistoga",serif;font-weight:400;font-size:20px;color:#fff}
.col-rule{width:35px;height:3px;background:var(--brand-yellow)}
.quick{left:410px;top:795px;list-style:none;font-size:14px;color:#eee}
.quick li{height:27px;display:flex;gap:9px}
.quick li::before{content:"»";font-size:12px}
.contact{font-size:14px;color:#eee;line-height:22px}
.contact b{font-weight:600;color:#fff}
.news-text{left:817px;top:794px;width:230px;font-size:13px;line-height:22px;color:#eee}
.news-form{left:817px;top:853px;width:221px;height:39px;background:#fff;font-family:"Merriweather",serif;font-weight:400;font-size:12.5px;color:#333;padding:11px 0 0 10px}
.news-form .send{position:absolute;right:0;top:0;width:39px;height:39px;background:var(--brand-yellow);display:flex;align-items:center;justify-content:center}
.bottom-band{left:0;top:1029px;width:1200px;height:53px;background:var(--brand-blue);color:#fff;font-size:13.5px}
.bottom-band .copy{position:absolute;left:163px;top:18px}
.bottom-band .pay{position:absolute;left:648px;top:18px}
.card-badge{position:absolute;top:14px;width:40px;height:24px;border-radius:2px;background:#fff}
</style>
</head>
<body>
<div class="page">

  <header>
    <div class="abs topbar">
      <span class="abs welcome">Welcome To BRENQUIL!</span>
      <span class="abs help">
        <svg width="16" height="12" viewBox="0 0 16 12"><rect x="0.5" y="0.5" width="15" height="11" fill="#fff"/><path d="M1 1 L8 7 L15 1 M1 11 L6 6 M15 11 L10 6" stroke="#000" stroke-width="1.2" fill="none"/></svg>
        <span><b>Need help?</b> help@brenquil.example</span>
      </span>
    </div>

    <div class="abs brand">BRENQUIL</div>

    <div class="abs search">Search Here
      <span class="btn"><svg width="13" height="13" viewBox="0 0 13 13"><circle cx="5.5" cy="5.5" r="4" stroke="#fff" stroke-width="1.8" fill="none"/><path d="M8.5 8.5 L12 12" stroke="#fff" stroke-width="1.8"/></svg></span>
    </div>

    <div class="abs account">
      <svg width="16" height="20" viewBox="0 0 16 20"><circle cx="8" cy="5" r="3.8" stroke="#222" stroke-width="1.6" fill="none"/><path d="M1 19 V14 Q1 10 8 10 Q15 10 15 14 V19 Z" stroke="#222" stroke-width="1.6" fill="none"/></svg>
      SIGN IN
    </div>
    <div class="abs cart">CART
      <svg width="28" height="24" viewBox="0 0 28 24"><path d="M1 2 H5 L8 16 H24 L27 6 H6" stroke="#222" stroke-width="1.8" fill="none"/><path d="M9 9 H25 M10 12.5 H24" stroke="#222" stroke-width="1.2"/><circle cx="11" cy="20" r="2" stroke="#222" stroke-width="1.6" fill="none"/><circle cx="21" cy="20" r="2" stroke="#222" stroke-width="1.6" fill="none"/></svg>
      <span class="count">0</span>
    </div>

    <div class="abs nav-rule"></div>
    <nav class="abs mainnav">
      <a class="current" style="left:0">HOME</a>
      <a style="left:81px">WOMEN <svg width="9" height="6" viewBox="0 0 9 6"><path d="M1 1 L4.5 4.5 L8 1" stroke="#222" stroke-width="1.8" fill="none"/></svg></a>
      <a style="left:187px">MEN <svg width="9" height="6" viewBox="0 0 9 6"><path d="M1 1 L4.5 4.5 L8 1" stroke="#222" stroke-width="1.8" fill="none"/></svg></a>
      <a style="left:267px">ABOUT</a>
      <a style="left:354px">CONTACT</a>
      <a style="left:458px">CATALOG</a>
    </nav>

    <div class="abs crumbs">
      <div class="trail"><span>HOME</span>
        <svg width="9" height="8" viewBox="0 0 9 8"><path d="M1 1 L4 4 L1 7 M5 1 L8 4 L5 7" stroke="#222" stroke-width="1.3" fill="none"/></svg>
        <span class="here">LOGIN</span></div>
    </div>
  </header>

  <main>
    <h1 class="abs login-title">Login</h1>
    <div class="abs login-card">
      <div class="field" style="top:35px">
        <span class="icon"><svg width="16" height="16" viewBox="0 0 16 16"><circle cx="8" cy="8" r="7.5" fill="#bbb"/><circle cx="8" cy="6" r="2.6" fill="#fff"/><path d="M3.5 13 Q8 8.5 12.5 13" fill="#fff"/></svg></span>
        <span class="hint">Username or email*</span>
      </div>
      <div class="field" style="top:88px">
        <span class="icon"><svg width="16" height="14" viewBox="0 0 16 14"><circle cx="4.5" cy="9.5" r="3" stroke="#bbb" stroke-width="1.8" fill="none"/><path d="M6.5 7.5 L13 1 M10 4 L12 6 M12 2 L14 4" stroke="#bbb" stroke-width="1.8"/></svg></span>
        <span class="hint">Password*</span>
        <svg class="eye" width="14" height="9" viewBox="0 0 14 9"><path d="M1 4.5 Q7 -2 13 4.5 Q7 11 1 4.5 Z" fill="#bbb"/><circle cx="7" cy="4.5" r="1.8" fill="#fff"/></svg>
      </div>
      <div class="login-btn">LOG IN</div>
      <div class="card-links"><a>Forgot Your Password?</a><span>New Customers? <a>Create Account</a></span></div>
    </div>
  </main>

  <footer>
    <svg class="abs site-footer" width="1200" height="369" viewBox="0 0 1200 369" preserveAspectRatio="none">
      <path fill="#333" d="M0 5 L40 3 L80 6 L120 2 L170 5 L220 3 L260 6 L310 2 L360 5 L400 4 L450 6 L500 2 L550 5 L600 3 L650 6 L700 2 L760 5 L810 3 L860 6 L910 2 L960 5 L1010 3 L1060 6 L1110 2 L1160 5 L1200 3 V369 H0 Z"/>
    </svg>

    <div class="abs footer-brand">BRENQUIL</div>
    <span class="abs social" style="left:224px"></span>
    <span class="abs social" style="left:261px"></span>

    <h3 class="abs col-title" style="left:410px;top:743px">Quick Links</h3>
    <div class="abs col-rule" style="left:411px;top:778px"></div>
    <ul class="abs quick">
      <li>Home</li><li>About</li><li>Contact</li><li>Catalog</li><li>Shipping</li><li>Returns</li>
    </ul>

    <h3 class="abs col-title" style="left:566px;top:743px">Contact Details</h3>
    <div class="abs col-rule" style="left:567px;top:778px"></div>
    <svg class="abs" style="left:566px;top:801px" width="12" height="17" viewBox="0 0 12 17"><path d="M6 16 Q0 8 0 6 A6 6 0 0 1 12 6 Q12 8 6 16 Z" fill="#fff"/><circle cx="6" cy="6" r="2.2" fill="#333"/></svg>
    <div class="abs contact" style="left:587px;top:799px">123 Building Name, Street<br>City Name, State 123456</div>
    <svg class="abs" style="left:566px;top:862px" width="14" height="14" viewBox="0 0 14 14"><path d="M3 0 L5.5 3.5 L4 5.5 Q6 9 8.5 10 L10.5 8.5 L14 11 L12 14 Q4 13 0 3 Z" fill="#fff"/></svg>
    <div class="abs contact" style="left:589px;top:859px"><b>PHONE</b><br>+1 123 456 7890</div>
    <svg class="abs" style="left:566px;top:921px" width="15" height="11" viewBox="0 0 15 11"><rect width="15" height="11" fill="#fff"/><path d="M0.5 0.5 L7.5 6 L14.5 0.5 M0.5 10.5 L5.5 5.5 M14.5 10.5 L9.5 5.5" stroke="#333" stroke-width="1.1" fill="none"/></svg>
    <div class="abs contact" style="left:589px;top:916px"><b>EMAIL</b><br>help@brenquil.example</div>

    <h3 class="abs col-title" style="left:817px;top:743px">Newsletter Subscribe</h3>
    <div class="abs col-rule" style="left:817px;top:778px"></div>
    <p class="abs news-text">Lorem ipsum dolor amet consetuer ading elit sed diam nonummy.</p>
    <div class="abs news-form">Email Address
      <span class="send"><svg width="18" height="16" viewBox="0 0 18 16"><path d="M0 7 L18 0 L13 16 L8 10 Z" fill="#222"/><path d="M8 10 L18 0" stroke="#FBC326" stroke-width="1.2"/></svg></span>
    </div>

    <div class="abs bottom-band">
      <span class="copy">Copyright 2020 Brenquil. All Rights Reserved.</span>
      <span class="pay">Payment We Accept</span>
      <span class="card-badge" style="left:798px"></span>
      <span class="card-badge" style="left:848px"></span>
      <span class="card-badge" style="left:897px"></span>
      <span class="card-badge" style="left:946px"></span>
      <span class="card-badge" style="left:995px"></span>
    </div>
  </footer>

</div>
</body>
</html>
```